2-Page Flyer for the Information Session about the Tranquil Venture Course

This is a flyer to announce/advertise an evening Information Session about the Tranquil Venture Course. This Program aims at mindfully rethinking and redesigning work (and life) for people who feel stuck or not entirely satisfied with their work and/or life (please see draft flyer attached for more details). This Program is property of Brightfold Joy, a company that uses a combination of Mindfulness, Design, and Entrepreneurship to help people achieve greater happiness (in their work and lives).
Updates

Target Market(s)

People who feel stuck or not entirely satisfied with their work and/or life (please see draft flyer attached for more details)

Font styles to use
Serif
Sans Serif

Colors
ffffff
f37122
33a6d7
acd037

Requirements
Must have
• All of what I will say below is suggestive (I’m not a design expert), and I’m open to divert from it, if it makes sense and feels more interesting.
• I thought initially of a 2-page flyer (please see draft flyer attached). The first page could help people grasp the essence of the event quickly (in 1 or 2 minutes), and then, if they are interested/motivated, they would continue reading through page 2, which has more info about the Program in itself.
• Potential Structure
• Page 1
• . About the Information Session on the Tranquil Venture Course
• . Visible Date & Time, Contacts, Venue (and other relevant info)
• . About me (the facilitator)
• Page 2
• . About the Tranquil Venture Course
• I include a Powerpoint draft of the flyer with the content. The design is rudimentary and precarious from an aesthetics/organization point of view, and this is mainly where I need help (and maybe in other aspects too!).
• On the flyer, I would like to include:
• . A photo of myself (I attach 1 picture).
• . 1 or 2 beautiful-nature photos (cropped or full). One may have to do with looking at the sky, dreaming, and imagining a new work and life (2 photos with sky and clouds attached). The other has to do with walking the transformation journey (the photo with the person walking through the forest path).
• . brightfold joy logo or logos (there are two slightly different ones, that can be used for different purposes). For the first page, I would like the brightfold joy logo that has "brightfold joy" written on the bottom, with the saying "Stillness, Craft and Venture for Joy" beneath. This is the main logo. For the 2nd page, you can choose the logo that adapts better.
• - Where it says the "the way out is in" it would be great to have a similar font to the one I attach (see file "Font_the_way_out_is_in.png" and Ankecallig-fg.ttf
Nice to have
• In terms of colours, I would not divert much from the logo colours (and of course white and black). I would like the flyer to be quite white. Almost like fairy-tale white: the white horse, the white snow, the white of the stars, the white heaven. White could be the base colour. White means peace, tranquillity, calm contentment, a smile.
• And then use the other colours. The green of the mindfulness. The blue of the sky, the dreams. And the orange of the sun, the energy, the fire, the action. And maybe the black for text.
• Where it says the "the way out is in" it would be great to have a similar font to the one I attach (see file "Font_the_way_out_is_in".
• I would like this flyer to be a piece of art, in every possible way. Simple, beautiful, ease, light, peaceful, calm happy. Just like the Tranquil Venture Course and brightfold joy Company that I am creating intends to be. The mission of this Program and Company is to be a designer, a painter (a Picasso) of happier and more fulfilling human lives.
• I am very much looking forward to seeing your proposal(s).

```html
<!DOCTYPE html>
<html lang="en">
<head>
<meta charset="utf-8">
<title>Tranquil Venture Course – Information Session Flyer</title>
<link rel="stylesheet" href="https://fonts.googleapis.com/css2?family=Libre+Caslon+Text:ital@1&family=Roboto:wght@400;700&display=swap">
<style>
  :root {
    --board: #e5e5e5;
    --paper: #ffffff;
    --ink: #1b1b1b;
    --soft-ink: #2a2a2a;
    --rule-blue: #7fc4e2;
    --tint-sky: #7cbde6;
    --tint-leaf: #c6d97a;
    --tint-sun: #f0a66c;
    --shape-grey: #e4e4e4;
    --mark-grey: #bdbdbd;
  }
  * { margin: 0; padding: 0; box-sizing: border-box; }
  h1, h2, p, li { font-weight: 400; }
  html, body { width: 1200px; height: 848px; overflow: hidden; }
  body {
    position: relative;
    background: var(--board);
    font-family: "Roboto", Arial, sans-serif;
    color: var(--ink);
  }
  .serif { font-family: "Libre Caslon Text", Georgia, serif; font-style: italic; font-weight: 400; }

  .pack-label {
    position: absolute; left: 71px; top: 53px; height: 88px;
    writing-mode: vertical-rl; transform: rotate(180deg);
    text-align: end;
    font-size: 7.6px; line-height: 12px; letter-spacing: 0.04em; color: var(--ink);
  }

  .page {
    position: absolute; top: 53px; width: 450px; height: 637px;
    background: var(--paper); overflow: hidden;
  }
  .page--one { left: 150px; }
  .page--two { left: 675px; }
  .page-number {
    position: absolute; top: 694px; font-size: 8px; letter-spacing: 0.06em; color: var(--ink);
  }
  .page-number--one { right: 603px; }
  .page-number--two { right: 78px; }

  .body-copy {
    position: absolute; font-size: 6.9px; line-height: 9.9px; letter-spacing: 0.07em; color: var(--soft-ink);
  }

  /* Page one */
  .program-title {
    position: absolute; left: 32px; top: 30px;
    font-size: 12px; line-height: 13.4px; letter-spacing: 0.42em; color: var(--ink);
  }
  .double-rule {
    position: absolute; left: 32px; top: 82px; width: 193px; height: 4px;
    border-top: 0.8px solid var(--ink); border-bottom: 0.8px solid var(--ink);
  }
  .event-details {
    position: absolute; right: 225px; top: 97px; text-align: right;
    font-size: 6.9px; line-height: 9.9px; letter-spacing: 0.07em; color: var(--soft-ink);
  }
  .event-details strong { font-weight: 700; color: var(--ink); letter-spacing: 0.08em; }
  .cover-art { position: absolute; left: 0; top: 0; }
  .cover-subtitle {
    position: absolute; left: 225px; top: 317px;
    font-size: 6.8px; line-height: 9.9px; letter-spacing: 0.08em; color: #ffffff;
  }
  .swatch { position: absolute; left: 79px; width: 18px; height: 18px; }
  .swatch--sky { top: 361px; background: var(--tint-sky); }
  .swatch--leaf { top: 385px; background: var(--tint-leaf); }
  .swatch--sun { top: 409px; background: var(--tint-sun); }

  .section-heading {
    position: absolute; font-size: 7.1px; letter-spacing: 0.08em; color: var(--ink);
    border-bottom: 0.7px solid var(--rule-blue); padding-bottom: 3px;
  }
  .mindfulness-heading { left: 225px; top: 529px; width: 193px; text-transform: uppercase; }
  .mindfulness-copy { left: 225px; top: 547px; }

  /* Page two */
  .course-heading { left: 34px; width: 191px; }
  .course-copy { left: 34px; }

  .outcomes-photo { position: absolute; left: 249px; top: 32px; }
  .outcomes-title {
    position: absolute; left: 302px; top: 54px;
    font-size: 10.5px; line-height: 13.6px; letter-spacing: 0.36em; color: var(--ink);
  }
  .outcomes-title .indent { padding-left: 20px; }
  .outcomes-dash { position: absolute; left: 322px; top: 88px; width: 9px; border-top: 0.8px solid var(--ink); }
  .outcomes-list { position: absolute; left: 322px; top: 94px; list-style: none; }
  .outcomes-list li {
    font-size: 6.9px; line-height: 9.9px; letter-spacing: 0.07em; color: var(--ink); margin-bottom: 9.6px;
  }

  .brand-rule { position: absolute; left: 322px; top: 307px; width: 97px; border-top: 0.7px solid var(--rule-blue); }
  .brand-name {
    position: absolute; left: 322px; top: 327px; display: flex; align-items: center; gap: 6px;
    font-size: 10px; letter-spacing: 0.08em; color: var(--ink); text-transform: uppercase;
  }
  .brand-square { width: 9px; height: 9px; background: var(--mark-grey); }
  .brand-contact {
    position: absolute; left: 322px; top: 361px;
    font-size: 4.5px; line-height: 7.6px; letter-spacing: 0.06em; color: var(--ink);
  }

  .closing-rule { position: absolute; left: 33px; top: 461px; width: 386px; border-top: 0.7px solid var(--rule-blue); }
  .facilitator-portrait { position: absolute; left: 32px; top: 501px; }
  .facilitator-bio {
    position: absolute; left: 167px; top: 499px; width: 254px;
    font-size: 4.5px; line-height: 7.6px; letter-spacing: 0.05em; color: var(--ink);
  }
  .facilitator-bio .name { font-weight: 700; }
  .facilitator-bio p + p { margin-top: 7.6px; }
</style>
</head>
<body>

<div class="pack-label">072019<br>BRIGHTFOLD JOY<br>INFORMATION PACK<br>001</div>

<section class="page page--one">
  <h1 class="program-title serif">THE TRANQUIL<br>VENTURE<br>COURSE</h1>
  <div class="double-rule"></div>

  <p class="event-details">
    <strong>FREE ENTRY</strong><br>
    Thursday 18th July 2019<br>
    19:30 - 21:00<br>
    Lumen Coworking<br>
    C/ Almendro 42<br>
    Barcelona
  </p>

  <svg class="cover-art" width="450" height="637" viewBox="0 0 450 637">
    <defs>
      <clipPath id="half-disc">
        <polygon points="300,40 430,40 417,91 354,154 300,154"/>
      </clipPath>
      <clipPath id="photo-disc">
        <circle cx="225" cy="318" r="143"/>
      </clipPath>
      <linearGradient id="lake" x1="0" y1="0" x2="0" y2="1">
        <stop offset="0" stop-color="#c9d2cf"/>
        <stop offset="0.28" stop-color="#7f9c99"/>
        <stop offset="0.45" stop-color="#2f6e70"/>
        <stop offset="0.52" stop-color="#3c8b8c"/>
        <stop offset="0.7" stop-color="#8aa9a5"/>
        <stop offset="0.85" stop-color="#8a7a66"/>
        <stop offset="1" stop-color="#4f4436"/>
      </linearGradient>
    </defs>

    <circle cx="385" cy="122" r="44" fill="var(--shape-grey)" clip-path="url(#half-disc)"/>

    <line x1="403" y1="140" x2="326" y2="216" stroke="#222" stroke-width="0.8"/>
    <line x1="123" y1="420" x2="45" y2="497" stroke="#222" stroke-width="0.8"/>
    <line x1="108" y1="462" x2="36" y2="534" stroke="#222" stroke-width="0.7" stroke-dasharray="5 5"/>

    <path d="M341,202 A164,164 0 0 1 109,434" fill="none" stroke="#333" stroke-width="0.6"/>

    <circle cx="225" cy="318" r="143" fill="url(#lake)" role="img" aria-label="Photograph of a calm mountain lake with rocky shore and misty peaks"/>

    <g class="serif" font-size="44" fill="var(--ink)">
      <text x="32" y="248" textLength="289" lengthAdjust="spacing">Information</text>
      <text x="226" y="294" textLength="178" lengthAdjust="spacing">Session</text>
    </g>
    <g class="serif" font-size="44" fill="#ffffff" fill-opacity="0.4" clip-path="url(#photo-disc)">
      <text x="32" y="248" textLength="289" lengthAdjust="spacing">Information</text>
      <text x="226" y="294" textLength="178" lengthAdjust="spacing">Session</text>
    </g>
  </svg>

  <p class="cover-subtitle">Key insights into the full Tranquil<br>Venture course</p>

  <span class="swatch swatch--sky"></span>
  <span class="swatch swatch--leaf"></span>
  <span class="swatch swatch--sun"></span>

  <h2 class="section-heading mindfulness-heading">What is mindfulness?</h2>
  <p class="body-copy mindfulness-copy">
    Mindfulness refers a sate of mind in which heightened<br>
    awareness and focus are achieved. To be mindful is<br>
    to be able to acknowledge your actions and emotions<br>
    in any particular moment. To give the entirety of your<br>
    attention to your current self, without contemplating<br>
    the past or worrying about the future.
  </p>
</section>
<div class="page-number page-number--one">PAGE ONE //</div>

<section class="page page--two">
  <h2 class="section-heading course-heading" style="top:31px">Why Does it Matter?</h2>
  <p class="body-copy course-copy" style="top:50px">
    Your time should be spent working on projects which<br>
    excite you and bring happiness into your life. This<br>
    course will connect you with people who can help you<br>
    reflect on your current situation, design your plan of<br>
    action and implement the steps necessary for you to<br>
    move in the right direction.
  </p>

  <h2 class="section-heading course-heading" style="top:130px">The Full Course</h2>
  <p class="body-copy course-copy" style="top:149px">
    The complete program entails four monthly sessions,<br>
    each five hours long, as well as a weekly two-hour<br>
    peer support meeting. The course is designed to<br>
    address both theory and practice regarding the<br>
    following topics.
  </p>

  <h2 class="section-heading course-heading" style="top:218px">Mindfulness Techniques</h2>
  <p class="body-copy course-copy" style="top:237px">
    We will discuss the various techniques involving<br>
    mindfulness and help you develop a more in-depth<br>
    understanding of how they can be used to improve<br>
    your life and your perception of work.
  </p>

  <h2 class="section-heading course-heading" style="top:297px">Design Thinking</h2>
  <p class="body-copy course-copy" style="top:316px">
    This term refers to the various processes involved in<br>
    the development of a creative concept. You will learn<br>
    how to make use of these same principles in order to<br>
    carry your ideas forward and make them actionable.
  </p>

  <h2 class="section-heading course-heading" style="top:376px">Entrepreneuship Framework</h2>
  <p class="body-copy course-copy" style="top:395px">
    You will be provided with resources and access to our<br>
    network, making it possible for you to implement what<br>
    you have learnt and start making impactful changes in<br>
    your own life.
  </p>

  <svg class="outcomes-photo" width="170" height="170" viewBox="0 0 170 170">
    <defs>
      <radialGradient id="leaves" cx="0.45" cy="0.4" r="0.7">
        <stop offset="0" stop-color="#d4dcd2"/>
        <stop offset="0.6" stop-color="#b7c4b4"/>
        <stop offset="1" stop-color="#9fb09c"/>
      </radialGradient>
    </defs>
    <circle cx="85" cy="85" r="85" fill="url(#leaves)" role="img" aria-label="Soft close-up photograph of green leaves with water droplets"/>
  </svg>
  <h2 class="outcomes-title serif">KEY<br><span class="indent">OUTCOMES</span></h2>
  <div class="outcomes-dash"></div>
  <ul class="outcomes-list">
    <li>Increased awareness,<br>clarity and confidence</li>
    <li>A deeper insight on what<br>makes you happy</li>
    <li>A clear design integrating<br>your ideal work-life balance</li>
    <li>Implementation of this<br>design to make impactful<br>changes in your own life</li>
  </ul>

  <div class="brand-rule"></div>
  <div class="brand-name"><span class="brand-square"></span>Brightfold Joy</div>
  <p class="brand-contact">
    Brought to you by Brightfold Joy<br>
    www.brightfoldjoy.com<br>
    info@brightfoldjoy.io
  </p>

  <div class="closing-rule"></div>

  <svg class="facilitator-portrait" width="104" height="104" viewBox="0 0 104 104">
    <defs>
      <linearGradient id="portrait-tone" x1="0" y1="0" x2="1" y2="1">
        <stop offset="0" stop-color="#9a9a9a"/>
        <stop offset="0.5" stop-color="#c8c8c8"/>
        <stop offset="1" stop-color="#e2e2e2"/>
      </linearGradient>
    </defs>
    <circle cx="52" cy="52" r="52" fill="url(#portrait-tone)" role="img" aria-label="Black and white portrait photograph of the course facilitator"/>
  </svg>

  <div class="facilitator-bio">
    <p><span class="name">Dr Marco Velloso</span><br>
      Visiting Research Fellow<br>
      Northbay University</p>
    <p>Having completed his PhD in Entrepreneurship at The University of Eastmere in 2014, Marco proceeded to joined the Northbay University as a Lecturer in Entrepreneurship the following year. His dissertation received the Halden Doctoral Dissertation Award from the Society of Enterprise Studies. His ideas and concepts are influenced by his industry experience in both sales and production engineering, as well as his time spent working as a strategy consultant with Riverside Business School after completing his MBA.</p>
    <p>Email: marco.velloso@brightfoldjoy.co.uk<br>
      Tel: +34 611 402 735<br>
      LinkedIn: amarcovelloso</p>
  </div>
</section>
<div class="page-number page-number--two">PAGE TWO //</div>

</body>
</html>
```